lunch and dinne(al a carte) menus

we are a medium sized licenced club that has taken back the dining in the club
in the western suburbs of sydney working class with a rugby league base
our logo is a wolf kelford hawks

Reason: We have changed the name to Bluegate grill it could be done as Bluegate or Bluegate or Bluegate We need a lunch menu and a seperate dinner menu eg Bluegate grill l u n c h or Bluegate grill d i n n e r

Reason: Weve changed the name

Target Market(s)

young families, working class rugby leagues sporty types

Industry/Entity Type

Club

Requirements
Must have
• user friendly

```html
<!DOCTYPE html>
<html lang="en">
<head>
<meta charset="utf-8">
<title>Kids Lunch Menu – Hawks Char Grill</title>
<link rel="stylesheet" href="https://fonts.googleapis.com/css2?family=Rye&family=Merriweather:wght@700&display=swap">
<style>
  :root {
    --charred-dark: #1c1a18;
    --charred-mid: #3a3632;
    --sign-wood-light: #f0d9a8;
    --sign-wood-dark: #d2b07a;
    --sign-edge: #8a6a3c;
    --sign-ink: #5a2f0c;
    --parchment-light: #fbf5de;
    --parchment-mid: #f3e9c4;
    --parchment-edge: #c9b98a;
    --menu-ink: #7b3f0b;
  }
  * { margin: 0; padding: 0; box-sizing: border-box; }
  html, body { width: 848px; height: 1200px; overflow: hidden; background: var(--charred-dark); }
  .menu-canvas { position: relative; width: 848px; height: 1200px; overflow: hidden; }
  .charred-wall {
    position: absolute; inset: 0;
    background:
      repeating-linear-gradient(180deg, transparent 0 84px, rgba(0,0,0,0.55) 84px 88px),
      radial-gradient(ellipse at 50% 50%, var(--charred-mid), var(--charred-dark) 75%);
  }
  .parchment { position: absolute; left: 0; top: 0; width: 848px; height: 1200px; }
  .wood-sign {
    position: absolute; left: 14px; width: 820px;
    background: linear-gradient(180deg, var(--sign-wood-light), var(--sign-wood-dark));
    border: 2px solid var(--sign-edge);
    box-shadow: 0 4px 10px rgba(0,0,0,0.6);
    display: flex; align-items: center; justify-content: center;
    overflow: hidden;
  }
  .wood-sign--top { top: 27px; height: 114px; }
  .wood-sign--bottom { top: 1063px; height: 113px; }
  .sign-title {
    font-family: "Rye", serif;
    font-weight: 400;
    color: var(--sign-ink);
    line-height: 1;
    white-space: nowrap;
  }
  .wood-sign--top .sign-title { font-size: 64px; letter-spacing: 3px; }
  .wood-sign--bottom .sign-title { font-size: 56px; letter-spacing: 3px; text-transform: uppercase; }
  .menu-list {
    position: absolute; left: 150px; top: 262px; width: 480px;
    font-family: "Merriweather", serif; font-weight: 700; color: var(--menu-ink);
  }
  .menu-item { margin-bottom: 70px; }
  .item-head { display: flex; justify-content: space-between; font-size: 34px; line-height: 56px; }
  .item-price { width: 32px; text-align: left; }
  .item-note { font-size: 34px; line-height: 56px; }
  .item-options { list-style: none; margin-top: 2px; }
  .item-options li { font-size: 25px; line-height: 44px; }
  .item-options li::before { content: "-"; }
</style>
</head>
<body>
<main class="menu-canvas">
  <div class="charred-wall" role="img" aria-label="Charred dark timber plank wall background"></div>

  <svg class="parchment" viewBox="0 0 848 1200" aria-hidden="true">
    <defs>
      <radialGradient id="parchment-fill" cx="50%" cy="48%" r="60%">
        <stop offset="0%" stop-color="#fbf5de"/>
        <stop offset="70%" stop-color="#f3e9c4"/>
        <stop offset="100%" stop-color="#c9b98a"/>
      </radialGradient>
    </defs>
    <path fill="url(#parchment-fill)" d="
      M110 150 L300 146 L330 140 L560 144 L640 138 L700 150 L690 175 L740 185 L745 230
      L790 240 L788 330 L770 360 L785 420 L760 470 L795 500 L820 560 L812 640 L775 690
      L760 760 L780 800 L770 870 L790 920 L775 990 L700 1010 L660 1030 L560 1050 L420 1045
      L300 1055 L200 1040 L150 1020 L120 1000 L125 930 L95 880 L70 820 L75 760 L60 700
      L25 660 L30 600 L60 560 L50 500 L80 460 L75 400 L55 360 L60 300 L100 270 L95 220
      L120 190 Z"/>
  </svg>

  <header class="wood-sign wood-sign--top">
    <h1 class="sign-title">Kids Lunch Menu</h1>
  </header>

  <section class="menu-list">
    <div class="menu-item">
      <div class="item-head"><span class="item-name">Sandwiches</span><span class="item-price">3</span></div>
      <ul class="item-options">
        <li>Yeast Spread</li>
        <li>Peanut Butter</li>
        <li>Choc Hazelnut</li>
        <li>Strawberry Jam</li>
        <li>Devon &amp; Tomato Sauce</li>
      </ul>
    </div>
    <div class="menu-item">
      <div class="item-head"><span class="item-name">Chicken Nuggets</span><span class="item-price">5</span></div>
      <p class="item-note">w/Chips</p>
    </div>
    <div class="menu-item">
      <div class="item-head"><span class="item-name">Cheese Burger</span><span class="item-price">5</span></div>
      <p class="item-note">w/Chips</p>
    </div>
  </section>

  <footer class="wood-sign wood-sign--bottom">
    <p class="sign-title">Hawks Char Grill</p>
  </footer>
</main>
</body>
</html>
```